Business Card Design

Certified KFL Instructor. Self defense instruction. Ladies classes available. Semi automatic and revolver

Industry/Entity Type

Defense

```html
<!DOCTYPE html>
<html lang="en">
<head>
<meta charset="utf-8">
<title>Dana Whitfield – Business Card</title>
<link rel="stylesheet" href="https://fonts.googleapis.com/css2?family=Bebas+Neue&family=Quicksand:wght@300;400&display=swap">
<style>
  :root {
    --page-bg: #e4e4e4;
    --card-bg: #ffffff;
    --accent-red: #ef5656;
    --accent-blue: #4bb8dc;
    --tag-text: #ffffff;
  }
  * { margin: 0; padding: 0; box-sizing: border-box; }
  html, body {
    width: 1200px;
    height: 898px;
    overflow: hidden;
    background: var(--page-bg);
  }
  .card {
    position: absolute;
    left: 180px;
    top: 209px;
    width: 840px;
    height: 480px;
    background: var(--card-bg);
    box-shadow: 0 6px 24px rgba(0,0,0,0.12);
    overflow: hidden;
  }
  .tag-band {
    position: absolute;
    left: 40px;
    top: 82px;
    width: 700px;
    height: 74px;
    background: var(--accent-red);
  }
  .holder-name {
    position: absolute;
    left: 44px;
    top: 34px;
    font-family: "Bebas Neue", sans-serif;
    font-size: 64px;
    line-height: 1;
    letter-spacing: 1px;
    color: var(--accent-blue);
  }
  .tagline {
    position: absolute;
    left: 56px;
    top: 104px;
    font-family: "Quicksand", sans-serif;
    font-weight: 300;
    font-size: 17px;
    line-height: 22px;
    text-transform: uppercase;
    color: var(--tag-text);
    letter-spacing: 0.3px;
  }
  .contact-list {
    position: absolute;
    left: 150px;
    top: 192px;
    list-style: none;
  }
  .contact-item {
    display: flex;
    align-items: center;
    height: 56px;
    font-family: "Quicksand", sans-serif;
    font-weight: 400;
    font-size: 32px;
    color: var(--accent-blue);
  }
  .contact-icon {
    width: 26px;
    height: 26px;
    margin-right: 26px;
    flex: none;
  }
  .stripe {
    position: absolute;
    left: 0;
    width: 100%;
    background: var(--accent-red);
  }
  .stripe-a { top: 378px; height: 5px; }
  .stripe-b { top: 392px; height: 11px; }
  .stripe-c { top: 440px; height: 5px; }
  .stripe-d { top: 453px; height: 11px; }
</style>
</head>
<body>
  <article class="card">
    <div class="tag-band"></div>
    <h1 class="holder-name">Dana Whitfield</h1>
    <p class="tagline">
      Certified KFL Instructor. Self defense instruction.<br>
      Ladies classes available. Semi automatic and revolver.
    </p>

    <ul class="contact-list">
      <li class="contact-item">
        <svg class="contact-icon" viewBox="0 0 26 26" aria-hidden="true">
          <circle cx="13" cy="7" r="5.5" fill="#ef5656"/>
          <path d="M3 25 V19 a6 6 0 0 1 6 -6 h8 a6 6 0 0 1 6 6 V25 Z" fill="#ef5656"/>
        </svg>
        <span>Dana Whitfield</span>
      </li>
      <li class="contact-item">
        <svg class="contact-icon" viewBox="0 0 26 26" aria-hidden="true">
          <rect x="1" y="5" width="24" height="17" fill="#ef5656"/>
          <path d="M1 5 L13 15 L25 5" fill="none" stroke="#ffffff" stroke-width="2"/>
        </svg>
        <span>dwhitfield@postmail.net</span>
      </li>
      <li class="contact-item">
        <svg class="contact-icon" viewBox="0 0 26 26" aria-hidden="true">
          <circle cx="13" cy="13" r="11.5" fill="none" stroke="#ef5656" stroke-width="2"/>
          <path d="M9 7.5 l2.2 -0.4 1.2 3 -1.5 1.2 a7 7 0 0 0 3.3 3.3 l1.2 -1.5 3 1.2 -0.4 2.2 a2 2 0 0 1 -2.2 1.5 a11 11 0 0 1 -8.3 -8.3 a2 2 0 0 1 1.5 -2.2 Z" fill="#ef5656"/>
        </svg>
        <span>601-555-0142</span>
      </li>
    </ul>

    <div class="stripe stripe-a"></div>
    <div class="stripe stripe-b"></div>
    <div class="stripe stripe-c"></div>
    <div class="stripe stripe-d"></div>
  </article>
</body>
</html>
```